Create Pop-Inspired Promo Designs for Orthodontic Contest: Velora Sparkle Fest

Velora Sparkle Fest Promotional Design Package

I need a creative graphic designer to develop a cohesive promotional design stand up banner for a 6-month orthodontic office contest called Velora Sparkle Fest — Bold Beams, Velora Dreams.

The campaign should feel modern, fun, and pop-inspired (musical, energetic, upbeat), while still professional and appropriate for a family orthodontic practice. Use of a female performer silhouette may be used on most material. I would like to use a silhouette version of Mirela Vantosh on the stand-up banner that will be stationed in the office.

Deliverables Needed

Retractable Stand-Up Banner (approx. 33x79)

Main waiting room announcement
Clean, bold visual impact
Minimal text, includes logo and contest title/tagline

Style Direction

Clean, modern, youthful
Pop-music-inspired elements (lights, gradients, abstract shapes)
White or light backgrounds preferred
Accent colors such as gold, blue, or soft pinks are welcome
Must feel polished, energetic, and consistent across all materials

Branding Provided

Practice logo files
Color preferences
Designer Expectations

Looking for someone with experience in promotional, event-style, or pop-inspired design work who can create a cohesive visual theme across multiple print formats.

Target Market(s)

Our orthodontic patients and families. This includes: Children (ages 6–12) Teens and pre-teens Young adults Parents who bring their children to appointments The designs should feel fun, energetic, upbeat, and modern—appealing especially to teens but still professional and appropriate for a healthcare office.

Industry/Entity Type

Orthodontic (Healthcare)

Requirements
Must have
• These elements must be included for the project to be successful: Clean, modern, pop-inspired visual style Prominent display of the contest name: Velora Sparkle Fest — Bold Beams, Velora Dreams Kettering Orthodontics logo on all materials White or light background (fresh, bright, professional)
Nice to have
• These are optional, but would enhance the final design: A generic female pop-star silhouette inspired by Mirela Vantosh’s style Subtle pop-music elements (stage lights, stars, mic shapes, gradients) Soft color accents such as gold, light blue, pinks, lilacs Slight sparkle or glossy “concert poster–style” effects Stylized motion elements or abstract energy lines A modern, youthful typeface pairing A cohesive mini-brand: consistent icons, shapes, or color motifs
Should not have
• No dark or cluttered backgrounds No overuse of neon or busy textures—avoid nightclub feel No childish cartoon illustrations No low-quality stock imagery No overly small text or cramped layouts No colors that clash with the orthodontic office’s professional aesthetic No references to prices, treatment incentives, or medical claims No heavy gradients or “loud” color mixes that distract from readability

```html
<!DOCTYPE html>
<html lang="en">
<head>
<meta charset="utf-8">
<title>Velora Sparkle Fest – Stand-Up Banner</title>
<link rel="stylesheet" href="https://fonts.googleapis.com/css2?family=Anton&family=Archivo+Black&family=Cinzel:wght@500&family=Great+Vibes&family=Monoton&family=Open+Sans:wght@700&family=Oswald:wght@500&family=Ubuntu:wght@500&display=swap">
<style>
  :root {
    --sky: #a9d6fb;
    --white: #ffffff;
    --brand-blue: #1b5fb0;
    --navy: #0b3f8f;
    --title-blue: #063d93;
    --line-blue: #1596f2;
    --gold: #ffe20a;
    --gold-edge: #b88a00;
    --pop-pink: #d65cf2;
    --ink: #000000;
    --band-light: #4a9fdc;
    --band-dark: #0c4596;
    --circle-top: #9d9be6;
    --circle-mid: #b8b4ee;
    --circle-low: #dfe0f8;
    --crowd-a: #3a6fc8;
    --crowd-b: #8fc3ec;
  }
  * { margin: 0; padding: 0; box-sizing: border-box; }
  html, body { width: 1200px; height: 2872px; overflow: hidden; }
  body {
    position: relative;
    background:
      radial-gradient(ellipse 520px 700px at 1200px 0, var(--sky) 0%, rgba(169,214,251,0) 100%),
      linear-gradient(180deg, #f6fbff 0%, #ffffff 55%, #eef5fd 100%);
  }
  .banner { position: absolute; inset: 0; }

  .practice-mark { position: absolute; left: 125px; top: 108px; display: flex; align-items: center; gap: 48px; }
  .practice-mark__square { width: 232px; height: 212px; background: var(--brand-blue); border-radius: 8px; }
  .practice-mark__name {
    font-family: "Cinzel", serif; font-weight: 500; color: var(--brand-blue);
    line-height: 1; text-transform: uppercase;
  }
  .practice-mark__name span { display: block; }
  .practice-mark__name .first { font-size: 98px; letter-spacing: 2px; }
  .practice-mark__name .second { font-size: 60px; margin-top: 14px; letter-spacing: 1px; }

  .contest-title {
    position: absolute; left: 0; width: 1200px; top: 420px; text-align: center;
    font-family: "Open Sans", sans-serif; font-weight: 700; font-size: 106px;
    color: var(--title-blue); letter-spacing: -1px; line-height: 1.1;
  }
  .contest-title__outline {
    position: absolute; left: 0; width: 1200px; top: 548px; text-align: center;
    font-family: "Monoton", sans-serif; font-size: 150px; color: var(--line-blue);
    letter-spacing: 14px; line-height: 1;
  }

  .spotlight-circle {
    position: absolute; left: 34px; top: 739px; width: 1132px; height: 1132px; border-radius: 50%;
    background: linear-gradient(160deg, var(--circle-top) 0%, var(--circle-mid) 40%, var(--circle-low) 75%, #f4f2fd 100%);
  }

  .tagline { position: absolute; left: 0; width: 1200px; text-align: center; }
  .tagline__script {
    top: 900px; font-family: "Great Vibes", cursive; font-size: 210px; line-height: 1;
    color: var(--gold); -webkit-text-stroke: 2px var(--gold-edge); z-index: 3;
  }
  .tagline__pop {
    top: 1030px; font-family: "Anton", sans-serif; font-size: 272px; line-height: 1;
    color: var(--pop-pink); -webkit-text-stroke: 4px var(--white);
    text-shadow: 0 10px 16px rgba(0,0,0,.35); letter-spacing: 4px;
  }
  .tagline__bold {
    top: 1330px; font-family: "Archivo Black", sans-serif; font-size: 196px; line-height: 1;
    color: var(--ink); -webkit-text-stroke: 3px var(--white);
    text-shadow: 0 10px 14px rgba(0,0,0,.35);
  }

  .crowd-photo {
    position: absolute; left: 0; top: 1540px; width: 1200px; height: 640px;
    background: linear-gradient(180deg, rgba(143,195,236,0) 0%, var(--crowd-b) 18%, var(--crowd-a) 45%, var(--crowd-b) 72%, rgba(255,255,255,0) 100%);
  }

  .message { position: absolute; left: 0; width: 1200px; text-align: center; line-height: 1; }
  .message__line1 { top: 2190px; font-family: "Archivo Black", sans-serif; font-size: 100px; color: var(--ink); letter-spacing: 4px; }
  .message__line2 { top: 2306px; font-family: "Archivo Black", sans-serif; font-size: 76px; color: var(--ink); letter-spacing: 3px; }
  .message__line3 { top: 2392px; font-family: "Oswald", sans-serif; font-weight: 500; font-size: 126px; color: var(--brand-blue); text-shadow: 0 4px 6px rgba(0,0,0,.3); }

  .footer-bands { position: absolute; left: 0; top: 2645px; width: 1200px; height: 227px; }
  .contact { position: absolute; font-family: "Ubuntu", sans-serif; font-weight: 500; color: var(--white); }
  .contact__phone { left: 143px; top: 2696px; font-size: 52px; letter-spacing: 1px; }
  .contact__web { left: 143px; top: 2752px; font-size: 32px; }
  .contact__address { left: 708px; top: 2742px; font-size: 35px; line-height: 48px; }
  .contact-icon { position: absolute; }
</style>
</head>
<body>
<main class="banner">
  <div class="practice-mark">
    <div class="practice-mark__square" aria-hidden="true"></div>
    <div class="practice-mark__name"><span class="first">Kettering</span><span class="second">Orthodontics</span></div>
  </div>

  <h1 class="contest-title">Velora Sparkle</h1>
  <div class="contest-title__outline">FEST</div>

  <div class="spotlight-circle" role="img" aria-label="Soft lilac-to-blue spotlight circle with a faint diamond light pattern"></div>

  <div class="tagline tagline__pop">VELORA</div>
  <div class="tagline tagline__bold">DREAMS</div>
  <div class="tagline tagline__script">Bold Beams</div>

  <div class="crowd-photo" role="img" aria-label="Photo of a concert crowd with raised hands, tinted blue and fading into white"></div>

  <div class="message message__line1">PRAESENT IN</div>
  <div class="message message__line2">URNA ELEMENTUM</div>
  <div class="message message__line3">AENEAN PORTTITOR</div>

  <svg class="footer-bands" viewBox="0 0 1200 227" aria-hidden="true">
    <polygon points="0,0 908,0 948,45 948,227 0,227" fill="var(--band-light)"/>
    <polygon points="663,53 1200,53 1200,227 468,227" fill="var(--band-dark)"/>
  </svg>

  <svg class="contact-icon" style="left:33px;top:2688px" width="92" height="92" viewBox="0 0 92 92" aria-hidden="true">
    <circle cx="46" cy="46" r="42" fill="none" stroke="#fff" stroke-width="6"/>
    <path d="M33 25c3-1 5 0 6 3l3 8c1 2 0 4-2 5l-3 2c2 6 7 11 13 14l2-3c1-2 3-3 5-2l8 3c3 1 4 3 3 6l-1 4c-1 3-4 4-7 4-18-2-33-17-35-35 0-3 1-6 4-7z" fill="#fff"/>
  </svg>
  <div class="contact contact__phone">+000 123 456 789</div>
  <div class="contact contact__web">www.websitename.com</div>

  <svg class="contact-icon" style="left:636px;top:2722px" width="54" height="80" viewBox="0 0 54 80" aria-hidden="true">
    <path d="M27 2C13 2 2 13 2 27c0 19 25 51 25 51s25-32 25-51C52 13 41 2 27 2zm0 35a10 10 0 1 1 0-20 10 10 0 0 1 0 20z" fill="#fff"/>
  </svg>
  <div class="contact contact__address">Your Street Address Here,<br>Zip Code Here - 000</div>
</main>
</body>
</html>
```